Rudy Fenwick - Free Personalised Health Consultation - "One size does not fit all"

This flyer will be left on tables/seats at speaking events and seminars and used to attain leads.

Top half will have "SMS me for a FREE Personalised Health Consultation" and my picture (see www.rudyfenwick.example and pick most engaging photo) and underneath my contact details. It must have lines with "Notes:" halfway down so people can take notes at the seminar and lines on the back with my contact details again and "Notes: with lines.

I am having a business card also being designed by Artshelf for same and would like the flyer and business card to carry a similar feel/look for consistency.

Below is the brief for the business card being designed:
Business Card for www.rudyfenwick.example site. It is a trust site and I use it for 1:1 relatable connections. It is the one I use for building intimate 1:1 trust building and Exec Coaching Services and programs for high wealth individuals and corporates. I also have a commercial programmatic site of my personal health products and services and programs for main stream one to many. www.quietbirchliving.example that can also provoke thought for the www.rudyfenwick.example business card. (mind you will get a separate business card for that site, but want to provide context). It has a logo which you may want to draw from in designing the rudyfenwick business card which is personal and is about building my brand. There is also a rudyfenwick personal FB page and rudyfenwick business FB page. I am a Certified Talent Compass 3.1 Coach with Harlow and you can get a corporate brief of me on there to give you more context https://www.harlowtalenthub.example/coach/en-us/directory?search=rudy

Target Market(s)

Exec, IT, Health conscious. Corporates wanting to run Health and Wellness programs. Those wanting to go from good to great. Millennials to Middleaged.

Industry/Entity Type

Health And Wellness

Font styles to use
Sans Serif
Other font styles liked:
• Arial and Calibri ok too

Colors

Designer to choose colors to be used in the design.

Requirements
Must have
• Picture of me - use best from www.rudyfenwick.example or can send one you choose.
• Contact details like my buisness card being designed by you guys in separate project.
• Name: Rudy Fenwick
• email: rudy@rudyfenwick.,example
• Phone: Australia +61 400 000 000 Singapore: +65 9000 0000
Nice to have
• Open to ideas

```html
<!DOCTYPE html>
<html lang="en">
<head>
<meta charset="utf-8">
<title>Rudy Fenwick – Free Personalised Health Consultation Flyer</title>
<link rel="stylesheet" href="https://fonts.googleapis.com/css2?family=Fira+Sans+Extra+Condensed:wght@500;600&family=Roboto:wght@400;500;700&display=swap">
<style>
  :root {
    --backdrop: #d8d5d1;
    --paper: #ffffff;
    --panel-dark: #262626;
    --footer-grey: #7b7b7b;
    --photo-light: #cfcfcf;
    --photo-mid: #8a8a8a;
    --photo-deep: #3a3a3a;
    --ink: #1e1e1e;
    --rule: #8c8c8c;
    --on-dark: #ffffff;
  }
  * { margin: 0; padding: 0; box-sizing: border-box; }
  html, body {
    width: 1200px; height: 903px; overflow: hidden;
    background: var(--backdrop);
    font-family: "Roboto", Arial, sans-serif;
  }
  .canvas { position: relative; width: 1200px; height: 903px; }

  .flyer {
    position: absolute; top: 80px;
    width: 526px; height: 744px;
    background: var(--paper);
    box-shadow: 0 2px 10px rgba(0,0,0,.25);
    overflow: hidden;
  }
  .flyer--front { left: 58px; }
  .flyer--back { left: 617px; }

  /* hero */
  .hero { position: absolute; left: 0; top: 0; width: 526px; height: 429px; }
  .hero__photo {
    position: absolute; inset: 0;
    background: linear-gradient(100deg, var(--photo-light) 0%, var(--photo-mid) 45%, var(--photo-deep) 100%);
  }
  .hero__panel { position: absolute; inset: 0; }
  .hero__copy {
    position: absolute; right: 59px; top: 130px;
    text-align: right; color: var(--on-dark);
  }
  .hero__lead {
    font-family: "Fira Sans Extra Condensed", "Arial Narrow", sans-serif;
    font-weight: 600; font-size: 43px; line-height: 1; letter-spacing: -0.5px;
  }
  .hero__free {
    font-family: "Fira Sans Extra Condensed", "Arial Narrow", sans-serif;
    font-weight: 600; font-size: 126px; line-height: .82; margin-top: 10px; letter-spacing: 1px;
  }
  .hero__offer {
    font-weight: 700; font-size: 28.5px; line-height: 1; margin-top: 12px; letter-spacing: -0.3px;
  }
  .hero__service {
    font-weight: 500; font-size: 18.4px; line-height: 1; margin-top: 8px;
  }
  .hero__signature {
    font-weight: 400; font-size: 15px; margin-top: 24px;
  }

  /* notes */
  .notes { position: absolute; left: 23px; right: 25px; }
  .flyer--front .notes { top: 442px; }
  .flyer--back .notes { top: 23px; }
  .notes__title {
    font-weight: 400; font-size: 20px; color: var(--ink); letter-spacing: .5px;
    height: 29px;
  }
  .notes__line {
    height: 40.6px;
    border-bottom: 1px dotted var(--rule);
  }
  .notes__line:first-of-type { height: 24px; }

  /* footer */
  .contact-bar { position: absolute; left: 0; bottom: 0; width: 526px; height: 43px; }
  .contact-bar svg { position: absolute; inset: 0; }
  .contact-bar__item {
    position: absolute; top: 14px;
    font-size: 11.5px; color: var(--on-dark); white-space: nowrap;
  }
  .contact-bar__divider {
    position: absolute; top: 9px; width: 1px; height: 22px; background: #8a8a8a;
  }
  .contact-bar__email { top: 12px; }
</style>
</head>
<body>
<main class="canvas">

  <!-- front -->
  <section class="flyer flyer--front">
    <div class="hero">
      <div class="hero__photo" role="img" aria-label="Black and white portrait of Rudy Fenwick standing beside a palm in a colonnade"></div>
      <svg class="hero__panel" width="526" height="429" viewBox="0 0 526 429" aria-hidden="true">
        <polygon points="266,22 526,22 526,429 262,429 190,226" fill="var(--panel-dark)" stroke="#ffffff" stroke-width="4"/>
        <rect x="520" y="20" width="8" height="412" fill="var(--panel-dark)"/>
        <rect x="258" y="426" width="270" height="5" fill="var(--panel-dark)"/>
      </svg>
      <div class="hero__copy">
        <p class="hero__lead">SMS me for a</p>
        <p class="hero__free">FREE</p>
        <p class="hero__offer">PERSONALISED</p>
        <p class="hero__service">HEALTH CONSULTATION</p>
        <p class="hero__signature">- Rudy Fenwick</p>
      </div>
    </div>

    <div class="notes">
      <h2 class="notes__title">NOTES</h2>
      <div class="notes__line"></div>
      <div class="notes__line"></div>
      <div class="notes__line"></div>
      <div class="notes__line"></div>
      <div class="notes__line"></div>
    </div>

    <footer class="contact-bar">
      <svg width="526" height="43" viewBox="0 0 526 43" aria-hidden="true">
        <rect width="526" height="43" fill="var(--panel-dark)"/>
        <polygon points="352,3 526,3 526,36 366,36" fill="var(--footer-grey)"/>
        <line x1="347" y1="3" x2="364" y2="43" stroke="#ffffff" stroke-width="2"/>
      </svg>
      <span class="contact-bar__item" style="left:38px">Australia +61 400 000 000</span>
      <span class="contact-bar__divider" style="left:183px"></span>
      <span class="contact-bar__item" style="left:192px">Singapore: +65 9000 0000</span>
      <span class="contact-bar__item contact-bar__email" style="left:369px">rudy@rudyfenwick.example</span>
    </footer>
  </section>

  <!-- back -->
  <section class="flyer flyer--back">
    <div class="notes">
      <h2 class="notes__title">NOTES</h2>
      <div class="notes__line"></div>
      <div class="notes__line"></div>
      <div class="notes__line"></div>
      <div class="notes__line"></div>
      <div class="notes__line"></div>
      <div class="notes__line"></div>
      <div class="notes__line"></div>
      <div class="notes__line"></div>
      <div class="notes__line"></div>
      <div class="notes__line"></div>
      <div class="notes__line"></div>
      <div class="notes__line"></div>
      <div class="notes__line"></div>
      <div class="notes__line"></div>
      <div class="notes__line"></div>
    </div>

    <footer class="contact-bar">
      <svg width="526" height="43" viewBox="0 0 526 43" aria-hidden="true">
        <rect width="526" height="43" fill="var(--panel-dark)"/>
        <polygon points="337,3 526,3 526,36 351,36" fill="var(--footer-grey)"/>
        <line x1="332" y1="3" x2="349" y2="43" stroke="#ffffff" stroke-width="2"/>
      </svg>
      <span class="contact-bar__item" style="left:24px">Australia +61 400 000 000</span>
      <span class="contact-bar__divider" style="left:169px"></span>
      <span class="contact-bar__item" style="left:177px">Singapore: +65 9000 0000</span>
      <span class="contact-bar__item contact-bar__email" style="left:360px">rudy@rudyfenwick.example</span>
    </footer>
  </section>

</main>
</body>
</html>
```